Venture firm needs flyer to attract Sales Professionals as Advisors

Creation of either a pdf Flyer or Brochure.
The target audience are senior sales professionals of the Information Technology industry. The flyer needs to come across highly professional, business oriented, positive. Text for the brochure is attached. The colors/graphics should align with Brindmore Capital corporate appearance: www.brindmore.capital

Target Market(s)

Sales Professionals in the Information Technology Industry

Industry/Entity Type

Information Technology

Font styles to use
• Raleway

Requirements
Must have
• fitting the corporate look and feel: www.brindmore.capital

```html
<!DOCTYPE html>
<html lang="en">
<head>
<meta charset="utf-8">
<title>Brindmore Capital – Momentum Sales Flyer</title>
<link rel="stylesheet" href="https://fonts.googleapis.com/css2?family=Raleway:ital,wght@0,300;0,400;0,500;0,600;0,700;0,800;1,600;1,700&display=swap">
<style>
  :root {
    --backdrop: #3a3a3c;
    --navy: #163c62;
    --navy-deep: #0f2f50;
    --mid-blue: #3f6e9c;
    --light-blue: #8fb2d6;
    --ice: #dfe8f1;
    --snow: #f4f7fa;
    --ink: #1d2a38;
    --white: #ffffff;
  }
  * { margin: 0; padding: 0; box-sizing: border-box; }
  html, body { width: 1200px; height: 777px; overflow: hidden; }
  body {
    background: var(--backdrop);
    font-family: "Raleway", sans-serif;
    position: relative;
  }
  .page {
    position: absolute;
    top: 28px;
    width: 510px;
    height: 720px;
    overflow: hidden;
    background: var(--white);
  }
  .page--front { left: 70px; }
  .page--back { left: 620px; }

  /* Front cover */
  .cover-photo {
    position: absolute; inset: 0;
    background: linear-gradient(160deg, #9fb4c9 0%, #c9d6e2 30%, #eef2f6 55%, #dfe7ef 100%);
  }
  .cover-shapes { position: absolute; inset: 0; }
  .cover-brand {
    position: absolute; left: 26px; top: 458px;
    font-size: 23px; font-weight: 400; letter-spacing: 1px;
    color: var(--white);
  }
  .cover-brand span { color: var(--light-blue); }
  .cover-kicker {
    position: absolute; left: 26px; top: 538px;
    font-size: 13.5px; font-weight: 400; color: var(--white);
  }
  .cover-title {
    position: absolute; left: 26px; top: 556px;
    font-size: 39px; font-weight: 700; letter-spacing: 0.5px;
    color: var(--white);
    padding-bottom: 4px;
    border-bottom: 1px solid var(--light-blue);
  }
  .cover-url {
    position: absolute; left: 44px; top: 680px;
    font-size: 15px; font-weight: 700; color: var(--white);
  }

  /* Back page */
  .header-art { position: absolute; left: 0; top: 0; width: 510px; height: 180px; }
  .header-title {
    position: absolute; left: 22px; top: 40px; color: var(--white);
  }
  .header-title strong {
    display: block; font-size: 26px; font-weight: 600; letter-spacing: 0.5px;
  }
  .header-title span {
    display: block; font-size: 14px; font-weight: 500; line-height: 1.2;
  }
  .header-tagline {
    position: absolute; right: 36px; top: 150px;
    font-size: 11.5px; font-weight: 700; color: var(--navy);
  }
  .section-tab {
    position: absolute; left: 0; top: 180px; width: 200px; height: 24px;
  }
  .section-tab span {
    position: absolute; left: 22px; top: 4px;
    font-size: 11.5px; font-weight: 700; color: var(--white);
  }
  .body-text {
    position: absolute; left: 34px; width: 450px;
    font-size: 8.4px; line-height: 1.32; font-weight: 500; color: var(--ink);
  }
  .body-text p + p { margin-top: 5px; }
  .about-text { top: 212px; }
  .works-badge {
    position: absolute; left: 50%; top: 290px; transform: translateX(-50%);
    background: var(--mid-blue); color: var(--white);
    font-size: 11px; font-weight: 700; padding: 4px 14px;
    border-bottom: 2px solid var(--navy);
  }
  .works-text { top: 322px; }
  .role-card {
    position: absolute; top: 470px; width: 210px; height: 136px;
    border: 1px solid var(--mid-blue);
    text-align: center; padding: 42px 14px 0;
  }
  .role-card--associates { left: 38px; }
  .role-card--advisors { left: 265px; top: 450px; height: 156px; }
  .role-icon {
    position: absolute; left: 50%; top: -22px; transform: translateX(-50%);
    width: 46px; height: 46px;
  }
  .role-card h3 {
    font-size: 12.5px; font-weight: 700; color: var(--navy); margin-bottom: 8px;
  }
  .role-card p { font-size: 7.8px; line-height: 1.3; font-weight: 500; color: var(--ink); }
  .footer-band { position: absolute; left: 0; top: 632px; width: 510px; height: 88px; }
  .footer-text {
    position: absolute; left: 30px; top: 660px; width: 460px;
    font-size: 9.6px; font-weight: 700; font-style: italic; line-height: 1.35;
    color: var(--white);
  }
</style>
</head>
<body>

<section class="page page--front">
  <div class="cover-photo" role="img" aria-label="Photograph of a mountaineer with an ice axe standing on a snowy ridge above a frozen lake"></div>
  <svg class="cover-shapes" viewBox="0 0 510 720" aria-hidden="true">
    <polygon points="0,222 160,300 160,312 0,236" fill="var(--mid-blue)"/>
    <polygon points="0,258 290,402 290,412 0,272" fill="var(--light-blue)" opacity="0.7"/>
    <polygon points="0,290 420,526 362,680 0,680" fill="var(--navy)"/>
    <polygon points="0,290 240,425 240,432 0,300" fill="var(--mid-blue)"/>
    <rect x="0" y="680" width="510" height="40" fill="var(--navy)"/>
    <polygon points="0,662 320,662 306,696 0,696" fill="var(--mid-blue)"/>
  </svg>
  <div class="cover-brand">BRINDMORE <span>CAPITAL</span></div>
  <div class="cover-kicker">Investing in Global Go-to-Market Strategies</div>
  <h1 class="cover-title">ACHIEVING GROWTH</h1>
  <div class="cover-url">www.brindmore.capital</div>
</section>

<section class="page page--back">
  <svg class="header-art" viewBox="0 0 510 180" aria-hidden="true">
    <rect width="510" height="180" fill="var(--mid-blue)"/>
    <rect width="200" height="180" fill="#5d86b0"/>
    <polygon points="200,0 470,0 470,180 160,180" fill="var(--snow)"/>
    <polygon points="470,0 490,0 490,180 470,180" fill="var(--mid-blue)"/>
    <polygon points="476,0 480,0 462,150 458,150" fill="var(--white)"/>
  </svg>
  <div role="img" aria-label="Photograph of a skier carving through powder snow on a mountain slope" style="position:absolute;left:210px;top:10px;width:240px;height:130px;background:radial-gradient(ellipse at 60% 40%, #e9eef3 0%, #c7d3df 70%, transparent 100%);"></div>
  <div class="header-title">
    <strong>Improve</strong>
    <span>Productivity with</span>
    <span>Momentum Sales</span>
  </div>
  <div class="header-tagline">Brindmore, built to grow strong</div>

  <svg class="section-tab" viewBox="0 0 200 24" aria-hidden="true">
    <polygon points="0,0 200,0 188,24 0,24" fill="var(--navy)"/>
  </svg>
  <div class="section-tab"><span>About Us:</span></div>

  <div class="body-text about-text">
    <p>The MSC is a by invitation only global community of high caliber Sales Professionals in the IT industry. Participating in the MSC provides significant wealth creation opportunities by earning consulting fees and sales commission or finding an exciting startup to work for.
    MSC members actively collaborate with each other to close deals, generate leads &amp; opportunities, navigate through client organizations and build a true advisory status with customers.
    MSC members get early first hand visibility into the latest technology innovations and learn how those technologies could assist their clients in solving their complex business objectives.</p>
  </div>

  <div class="works-badge">HOW IT WORKS:</div>

  <div class="body-text works-text">
    <p>MSC members will be introduced to Brindmore Capital' client and portfolio companies. This unique ability to learn about latest technology innovation keeps the participants up to date with industry trends and could open interesting earning or employment opportunities.</p>
    <p>Once exposed to a specific vendor, MSC members can decide if and how they would like to get further involved. Dependent on the interest level for the specific technology, the ability to offer a solution to a known customer problem or the sheer interest to develop new business, MSC members can participate in two ways:</p>
  </div>

  <div class="role-card role-card--associates">
    <svg class="role-icon" viewBox="0 0 46 46" aria-hidden="true">
      <circle cx="23" cy="23" r="23" fill="var(--navy)"/>
      <circle cx="17" cy="17" r="5" fill="var(--white)"/>
      <circle cx="29" cy="17" r="5" fill="var(--white)"/>
      <path d="M9 34 q0-10 8-10 q8 0 8 10z M21 34 q0-10 8-10 q8 0 8 10z" fill="var(--white)"/>
    </svg>
    <h3>As Associates:</h3>
    <p>Associates are actively selling and promoting one or more Brindmore Capital' portfolio companies. This could be an employment or a freelance opportunity.</p>
  </div>

  <div class="role-card role-card--advisors">
    <svg class="role-icon" viewBox="0 0 46 46" aria-hidden="true">
      <circle cx="23" cy="23" r="23" fill="var(--navy)"/>
      <circle cx="23" cy="13" r="5" fill="var(--white)"/>
      <path d="M16 36 v-12 q0-5 7-5 q7 0 7 5 v12z" fill="var(--white)"/>
      <line x1="30" y1="22" x2="37" y2="12" stroke="var(--white)" stroke-width="1.5"/>
    </svg>
    <h3>As Advisors:</h3>
    <p>Advisors offer their contacts and knowledge about customers to Associates.Advisors could create leads, support with introductions, explain customer organization and processes etc. They will be compensated by Associates with a pre-negotiated % of commission of a future sale that was supported by the Advisor.</p>
  </div>

  <svg class="footer-band" viewBox="0 0 510 88" aria-hidden="true">
    <polygon points="0,14 250,14 262,0 274,14 510,14 510,88 0,88" fill="var(--navy)"/>
  </svg>
  <p class="footer-text">Whatever level of involvement a MSC member seeks there is plenty of opportunity to be rewarded for working with fellow Sales Professionals and Great Startups on the forefront of technical innovation.</p>
</section>

</body>
</html>
```